Corvel Lease Homes
will not have subtitle
Corvel Lease Homes -
Creative Brief
Simple
Paul Venner, Tessa Venner
PO Box 58211 20415 #7 Rd Surrey, BC V2T 5K9
info@corvelholdings.ca
www.corvelholdings.ca
On front- white background with small logo and our contact info. Paul's # is 604.555.0187, mine is the other. would like all the colors to be the same as logo and info in blue. Back- blue background with large logo. I would also be interested in simply seeing what you all come up with as you know what looks best-so feel free to do something different than what I said and we'll go from there. Thank you.

```html
<!DOCTYPE html>
<html lang="en">
<head>
<meta charset="utf-8">
<title>Corvel Lease Homes – Business Card</title>
<link rel="stylesheet" href="https://fonts.googleapis.com/css2?family=Tinos:wght@400;700&display=swap">
<style>
  :root {
    --backdrop: #3a3d40;
    --card-white: #ffffff;
    --brand-blue: #1d5a96;
    --brand-blue-deep: #123e73;
    --brand-blue-light: #3f86c6;
    --ink: #2a2a2a;
    --divider: #6b7c8f;
  }
  * { margin: 0; padding: 0; box-sizing: border-box; }
  html, body {
    width: 1200px; height: 751px; overflow: hidden;
    background: var(--backdrop);
    font-family: "Tinos", "Times New Roman", serif;
  }
  .canvas { position: relative; width: 1200px; height: 751px; }

  .card { position: absolute; border-radius: 26px; overflow: hidden; }

  .card-front {
    left: 259px; top: 43px; width: 617px; height: 312px;
    background: var(--card-white);
    box-shadow: 0 6px 18px rgba(0,0,0,.35);
  }
  .front-swoosh { position: absolute; left: 0; bottom: 0; width: 100%; height: 60px; }

  .brand-name {
    position: absolute; left: 0; right: 0; top: 62px;
    text-align: center; color: var(--brand-blue);
    font-size: 36px; font-weight: 700; letter-spacing: 1px;
  }

  .contact { position: absolute; top: 152px; left: 0; right: 0; height: 110px; }
  .people {
    position: absolute; right: 392px; top: 0; text-align: right; color: var(--ink);
  }
  .person-name { font-size: 22px; line-height: 24px; }
  .person-phone { font-size: 11px; line-height: 16px; margin-bottom: 4px; }
  .contact-divider {
    position: absolute; left: 245px; top: 2px; width: 1px; height: 102px;
    background: var(--divider);
  }
  .details {
    position: absolute; left: 258px; top: 4px; color: var(--ink);
    font-size: 12px; line-height: 16px;
  }
  .details b { font-weight: 700; color: var(--brand-blue); }

  .card-back {
    left: 583px; top: 391px; width: 540px; height: 320px;
    background: radial-gradient(ellipse at 55% 50%, var(--brand-blue-light) 0%, var(--brand-blue) 45%, var(--brand-blue-deep) 100%);
    box-shadow: 0 6px 18px rgba(0,0,0,.4);
  }
  .card-back .brand-name {
    top: 128px; color: var(--card-white); font-size: 40px;
  }
</style>
</head>
<body>
<main class="canvas">
  <section class="card card-front" aria-label="Card front">
    <div class="brand-name">Corvel Lease Homes</div>
    <div class="contact">
      <div class="people">
        <div class="person-name">Paul Venner</div>
        <div class="person-phone">604.555.0187</div>
        <div class="person-name">Tessa Venner</div>
        <div class="person-phone">604.555.0142</div>
      </div>
      <div class="contact-divider"></div>
      <div class="details">
        <div>PO Box 58211 | 20415 #7 Rd</div>
        <div>Surrey, BC | V2T 5K9</div>
        <div><b>F</b> : 604.555.0196</div>
        <div><b>E</b> : info@corvelholdings.ca</div>
        <div><b>W</b> : www.corvelholdings.ca</div>
      </div>
    </div>
    <svg class="front-swoosh" viewBox="0 0 617 60" preserveAspectRatio="none" aria-hidden="true">
      <defs>
        <linearGradient id="swooshFill" x1="0" x2="1" y1="0" y2="0">
          <stop offset="0" stop-color="#123e73"/>
          <stop offset="0.5" stop-color="#3f86c6"/>
          <stop offset="1" stop-color="#123e73"/>
        </linearGradient>
      </defs>
      <path d="M0 30 Q308 62 617 30 L617 60 L0 60 Z" fill="url(#swooshFill)"/>
      <path d="M0 22 Q308 54 617 22" fill="none" stroke="#3f86c6" stroke-width="2" opacity=".6"/>
    </svg>
  </section>

  <section class="card card-back" aria-label="Card back">
    <div class="brand-name">Corvel Lease Homes</div>
  </section>
</main>
</body>
</html>
```